Name of Business: KUR Advisory. It is a consulting and advisory business providing Investment and f

I am looking for a letterhead (preferably in word) design for a new business that portarys the attributes of professionalism, honesty, integrity and impartiality. I operate in a Regional area called Ocean Grove which is located about 90min drive from Melbourne CBD on the Victorian coast.

I have an open mind on design and colour: like all things creative it will either hit the spot or not.

Hi - Thank you all for your disigns. We are currently travelling in Australia and can't always get an internet coonnections. We are reviewing all designs and will try and get back to each of your over the next few days. Dennis Walbrook

```html
<!DOCTYPE html>
<html lang="en">
<head>
<meta charset="utf-8">
<title>KUR Advisory — Stationery</title>
<link href="https://fonts.googleapis.com/css2?family=Open+Sans:wght@300;400;600;700&family=Mr+De+Haviland&display=swap" rel="stylesheet">
<style>
  :root {
    --brand-red: #b5443b;
    --brand-red-soft: #c9665d;
    --watermark: #f1e4e2;
    --ink: #1f1f1f;
    --paper: #f6f6f6;
    --card-white: #f9f9f9;
    --backdrop: #ebebeb;
  }
  * { margin: 0; padding: 0; box-sizing: border-box; }
  html, body { width: 1200px; height: 1000px; overflow: hidden; }
  body {
    background: var(--backdrop);
    font-family: "Open Sans", Arial, sans-serif;
    color: var(--ink);
    position: relative;
  }

  .letterhead {
    position: absolute; left: 123px; top: 75px;
    width: 602px; height: 852px;
    background: var(--paper);
    overflow: hidden;
  }
  .brand-name {
    position: absolute; left: 66px; top: 48px;
    font-weight: 700; font-size: 30px; line-height: 1;
    color: var(--brand-red); letter-spacing: -0.5px;
  }
  .contact {
    position: absolute; right: 70px; top: 58px;
    text-align: right; font-size: 9px; line-height: 13px;
  }
  .contact b { font-weight: 700; }

  .letter-title {
    position: absolute; left: 173px; top: 225px; width: 359px;
    text-align: center; font-size: 11px; font-weight: 700;
  }

  .meta { position: absolute; right: 445px; text-align: right; font-size: 11px; line-height: 15px; }
  .meta dt { font-weight: 700; }
  .meta-date { top: 269px; }
  .meta-from { top: 331px; }
  .meta-to { top: 423px; }

  .letter-body {
    position: absolute; left: 173px; top: 269px; width: 359px;
    font-size: 11px; line-height: 14.8px; text-align: justify;
  }
  .letter-body p { text-indent: 12px; }
  .letter-body p.gap { margin-top: 15px; }

  .signature {
    position: absolute; left: 172px; top: 700px;
    font-family: "Mr De Haviland", cursive; font-size: 24px; line-height: 1;
  }
  .signature-role {
    position: absolute; left: 192px; top: 729px;
    font-size: 7px; letter-spacing: 0.3px;
  }

  .watermark {
    position: absolute; left: 388px; top: 700px;
    font-weight: 700; font-size: 62px; line-height: 1;
    color: var(--watermark); white-space: nowrap; letter-spacing: -1px;
  }

  .card { position: absolute; width: 260px; height: 144px; }
  .card-front {
    left: 820px; top: 512px; background: var(--brand-red);
    display: flex; align-items: center; justify-content: center;
  }
  .card-front .brand-name-card {
    font-weight: 700; font-size: 28px; color: #ffffff; letter-spacing: -0.5px;
  }
  .card-back { left: 817px; top: 733px; width: 258px; background: var(--card-white); }
  .services {
    position: absolute; left: 0; right: 0; top: 44px;
    text-align: center; font-weight: 300; font-size: 17px; line-height: 17px;
    color: var(--brand-red);
  }
  .services .soft { color: var(--brand-red-soft); }
  .services .strong { font-weight: 400; }
  .card-details {
    position: absolute; left: 0; right: 0; top: 130px;
    text-align: center; font-size: 4.6px; white-space: nowrap;
  }
  .card-details b { font-weight: 700; }
</style>
</head>
<body>

<section class="letterhead">
  <div class="brand-name">KUR Advisory</div>

  <address class="contact">
    <div><b>PHONE</b> 000 000 000</div>
    <div><b>PHONE</b> 000000 0000</div>
    <div>str. Elm 12, City, Earth</div>
    <div>mail@kuradvisory.com.au</div>
  </address>

  <h1 class="letter-title">Lorem ipsum dolor sit amet, ei eros vidit sonet eum</h1>

  <dl class="meta meta-date"><dt>Date</dt><dd>September 25, 2014</dd></dl>
  <dl class="meta meta-from"><dt>From</dt><dd>Mr. Ivan Lorne</dd><dd>Financial Director</dd><dd>Investments</dd></dl>
  <dl class="meta meta-to"><dt>To</dt><dd>Mr. Simon Hale</dd><dd>CEO Business Solution</dd></dl>

  <div class="letter-body">
    <p>Lorem ipsum dolor sit amet, ei eros vidit sonet eum, sed ea aliquam offendit. Reque quando labitur nec in, no solum ceteros est. Accumsan pertinacia an qui. Te vidisse recteque pro, cu per habemus officiis, eos ex malis posidonium omittantur.</p>
    <p>Lorem ipsum dolor sit amet, ei eros vidit sonet eum, sed ea aliquam offendit. Reque quando labitur nec in, no solum ceteros est. Accumsan pertinacia an qui. Te vidisse recteque pro, cu per habemus officiis, eos ex malis posidonium omittantur. Appetere principes eloquentiam vis ei, an mea alia petentium dignissim, te justo omnium duo.</p>
    <p class="gap">Movet laoreet delicatissimi cum id. Essent dissentiet cu cum, atqui augue iriure qui ea. Liber propriae ei sed. Euismod ornatus scaevola et pro.</p>
    <p class="gap">Verterem interesset disputationi vim et, laudem persecuti quo eu. Mea viderer vulputate ut. Ad scripta scaevola appetere usu, omnium forensibus sed cu, dolorum admodum postulant mea ei. Eos ut ubique graeco insolens, etiam electram assentior cum at.</p>
    <p class="gap">In eos solum verterem facilisis, magna scaevola explicari has ex, at vidisse percipitur cum. At dicam postea luptatum sea, sed te timeam principes disputando, postea scaevola eloquentiam quo eu. Cetero concludaturque cu ius, nam erat detraxit ut, in his cetero vocent erroribus. Eu sint nulla comprehensam qui. Dolor dolorum splendide ei est, id usu inani liber deterruisset.</p>
  </div>

  <div class="signature">Signature</div>
  <div class="signature-role">NAME / C.E.O</div>

  <div class="watermark" aria-hidden="true">KUR Advisory</div>
</section>

<section class="card card-front">
  <div class="brand-name-card">KUR Advisory</div>
</section>

<section class="card card-back">
  <div class="services">
    <div class="soft">CONSULTING</div>
    <div>ADVISORY</div>
    <div class="strong">BUSINESS</div>
  </div>
  <div class="card-details"><b>PHONE:</b> 000 000 000 / <b>FAX:</b> 000000 0000 / <b>STREET:</b> Elm 12, City, Earth / <b>EMAIL:</b> mail@kuradvisory.com.au</div>
</section>

</body>
</html>
```